Company Profile
Korvane Cargo Sdn Bhd is a well-established and experienced freight forwarder in Kuala Lumpur, Malaysia. We specialize in air and sea forwarding, Custom Brokerage and regulatory compliance services, inland transportation, overseas freighting and warehousing and distribution management. With our dedicated qualified and experienced professionals, we are fully committed to serving our clients.

Our Mission
Based on the motto “Quick, Reliable and Polite”, Korvane Cargo is dedicated to upholding the following three points corporate philosophy:1. Adhering to the principle that “the customer always comes first”.2. Contributing to the development of the local community.3. Making it our duty to be responsible and sincere.

Our Edge
• One-Stop Logistics Solutions
• Extensive Network Throughout Malaysia
• Highly Qualified and Experienced Pool of Professionals
• Comprehensive IT Solutions
• Innovative and Customer-focused Solutions
• Flexible and Consistent in Managing Exceptions
• Total Supply Chain Visibility

Target Market : We sell the logistics services to all the industry in Malaysia. (One Stop Logistics Solutions)

Business Card Detail : I would like to see the logo on the front with the general info.

Must Haves :
1) Name, Title, Office, Cell, Fax, Email, Address, Website
2) Must have complete company name show as : Korvane Cargo Sdn Bhd
3) Must have company registration no, show as : 8571620-W

Nice to Haves : Modern Design Business Card

Target Market(s)

We sell the logistics services to all the industry in Malaysia. (One Stop Logistics Solutions)

Contact Information for Business Card

I would like to see the logo on the front with the general info.

Colors

Designer to choose colors to be used in the design.

Requirements
Must have
• 1) Name, Title, Office, Cell, Fax, Email, Address, Website
• 2) Must have complete company name show as : Korvane Cargo Sdn Bhd
• 3) Must have company registration no, show as : 8571620-W
Nice to have
• Modern Design Business Card
Should not have
• Nil

```html
<!DOCTYPE html>
<html lang="en">
<head>
<meta charset="utf-8">
<title>Korvane Cargo – Business Card</title>
<link rel="stylesheet" href="https://fonts.googleapis.com/css2?family=Arimo:ital,wght@0,400;0,700;1,700&family=Exo+2:wght@600&display=swap">
<style>
  :root {
    --page-bg: #d6d2cb;
    --navy-deep: #0c1f4a;
    --navy-mid: #173a75;
    --navy-light: #24528f;
    --accent-blue: #2a7cc4;
    --frost: #e4e7ea;
    --frost-edge: #cfd4d9;
    --text-light: #eef1f6;
    --text-soft: #d3dae6;
    --logo-ink: #0f2550;
  }
  * { margin: 0; padding: 0; box-sizing: border-box; }
  html, body { width: 1200px; height: 970px; overflow: hidden; }
  body { background: var(--page-bg); position: relative; font-family: "Arimo", Arial, sans-serif; }

  .business-card {
    position: absolute; left: 60px; top: 178px;
    width: 1080px; height: 614px;
    border-radius: 34px; overflow: hidden;
    background: linear-gradient(135deg, var(--frost) 0%, #f1f3f5 50%, var(--frost-edge) 100%);
    box-shadow: 0 18px 40px rgba(0,0,0,0.18);
  }
  .card-shapes { position: absolute; inset: 0; }

  .contact-side { position: absolute; left: 57px; top: 0; color: var(--text-soft); }
  .person-name {
    position: absolute; top: 62px; white-space: nowrap;
    font-family: "Exo 2", sans-serif; font-weight: 600; font-size: 34px; color: var(--text-light);
  }
  .person-title { position: absolute; top: 104px; white-space: nowrap; font-size: 25px; color: var(--text-soft); }
  .company-name {
    position: absolute; top: 163px; white-space: nowrap;
    font-style: italic; font-weight: 700; font-size: 27px; color: var(--text-light);
  }
  .company-reg {
    position: absolute; top: 197px; white-space: nowrap;
    font-style: italic; font-weight: 700; font-size: 22px; color: var(--text-light);
  }
  .address { position: absolute; top: 240px; font-size: 25px; line-height: 34px; white-space: nowrap; }
  .contact-list { position: absolute; top: 395px; list-style: none; font-size: 23px; line-height: 30px; white-space: nowrap; }
  .contact-list li { display: flex; align-items: center; gap: 18px; }
  .contact-list svg { width: 20px; height: 20px; flex: none; fill: var(--text-soft); }
  .contact-list .web { letter-spacing: 1.5px; }

  .brand-side {
    position: absolute; left: 620px; top: 0; width: 420px; height: 614px;
    display: flex; align-items: center; justify-content: center; gap: 20px;
  }
  .brand-circle { width: 54px; height: 54px; border-radius: 50%; border: 6px solid var(--logo-ink); flex: none; }
  .brand-name {
    font-family: "Arimo", Arial, sans-serif; font-weight: 700; font-size: 44px;
    line-height: 50px; letter-spacing: 3px; color: var(--logo-ink);
  }
</style>
</head>
<body>
  <div class="business-card">
    <svg class="card-shapes" viewBox="0 0 1080 614" width="1080" height="614">
      <defs>
        <linearGradient id="panelFill" x1="0" y1="0" x2="1" y2="1">
          <stop offset="0" stop-color="var(--navy-light)"/>
          <stop offset="0.45" stop-color="var(--navy-mid)"/>
          <stop offset="1" stop-color="var(--navy-deep)"/>
        </linearGradient>
      </defs>
      <path d="M0,0 H566 Q417,307 560,614 H0 Z" fill="url(#panelFill)"/>
      <path d="M581,0 Q430,307 576,614" fill="none" stroke="var(--accent-blue)" stroke-width="5"/>
      <path d="M589,0 Q440,307 584,614" fill="none" stroke="#ffffff" stroke-opacity="0.6" stroke-width="1.5"/>
    </svg>

    <div class="contact-side">
      <div class="person-name">Daniel Tan</div>
      <div class="person-title">Managing Director</div>
      <div class="company-name">Korvane Cargo Sdn Bhd</div>
      <div class="company-reg">8571620-W</div>
      <p class="address">No.28B, 2nd Floor<br>Jalan Kenari Indah 3B/KS4<br>Taman Seri Pantai, 41150 Klang<br>Selangor Darul Ehsan, Malaysia</p>
      <ul class="contact-list">
        <li><svg viewBox="0 0 20 20"><path d="M6 1h8a1 1 0 0 1 1 1v16a1 1 0 0 1-1 1H6a1 1 0 0 1-1-1V2a1 1 0 0 1 1-1zm1 2v12h6V3zm3 13a1 1 0 1 0 0 2 1 1 0 0 0 0-2z"/></svg>(+6012) 555 0192</li>
        <li><svg viewBox="0 0 20 20"><path d="M2 6c0-2 3-3 8-3s8 1 8 3v1h-4V5.5H6V7H2zm3 3h10l2 8H3zm5 2a2.5 2.5 0 1 0 0 5 2.5 2.5 0 0 0 0-5z"/></svg>(+603) 5550 2817 / 2818</li>
        <li><svg viewBox="0 0 20 20"><path d="M5 2h10v5H5zM2 8h16v7h-3v3H5v-3H2zm5 5v4h6v-4z"/></svg>(+603) 5550 2819</li>
        <li><svg viewBox="0 0 20 20"><path d="M2 4h16v12H2zm2 2v.5l6 4.5 6-4.5V6zm0 3v5h12V9l-6 4.5z"/></svg>daniel.tan@korvanecargo.com.my</li>
        <li><svg viewBox="0 0 20 20"><path d="M10 1a9 9 0 1 0 0 18 9 9 0 0 0 0-18zm-1 2.1V6H6.2A7 7 0 0 1 9 3.1zm2 0A7 7 0 0 1 13.8 6H11zM3.5 8H7v4H3.5a7 7 0 0 1 0-4zM9 8h2v4H9zm4 0h3.5a7 7 0 0 1 0 4H13zm-6.8 6H9v2.9A7 7 0 0 1 6.2 14zm4.8 0h2.8a7 7 0 0 1-2.8 2.9z"/></svg><span class="web">www.korvanecargo.com.my</span></li>
      </ul>
    </div>

    <div class="brand-side">
      <span class="brand-circle" aria-hidden="true"></span>
      <div class="brand-name">KORVANE<br>CARGO</div>
    </div>
  </div>
</body>
</html>
```